Industrial Professional Business Card Design (Vantrel Systems)

Would like professional looking business cards. Not too busy leaning towards minimal. Should have a slogan like:
"Industrial Automation and Control".

We are a tech company that programs industrial PLC computers. We also develop custom hardware solutions. Please use the logo for inspiration.

Target Market(s)

Mining, industrial, processing, automation, factory

Industry/Entity Type

Engineering

Contact Information for Business Card

Name, phone, email, website. job title.

Font styles to use
Other font styles liked:
• droid sans

Requirements
Must have
• Use colours that go well with the logo. Not too busy design.

```html
<!DOCTYPE html>
<html lang="en">
<head>
<meta charset="utf-8">
<title>Vantrel Systems — Business Card</title>
<link rel="stylesheet" href="https://fonts.googleapis.com/css2?family=Open+Sans:wght@400;600;700&display=swap">
<style>
  :root {
    --navy: #174a72;
    --orange: #ee6a1f;
    --white: #ffffff;
    --paper: #fbfcfd;
    --backdrop: #3a3d42;
    --ink-soft: rgba(255,255,255,0.8);
  }
  * { margin: 0; padding: 0; box-sizing: border-box; }
  html, body {
    width: 1200px; height: 900px; overflow: hidden;
    background: var(--backdrop);
    font-family: "Open Sans", sans-serif;
  }
  .sheet { position: relative; width: 1200px; height: 900px; }
  .card {
    position: absolute; left: 250px; width: 700px; height: 400px;
    border-radius: 22px; overflow: hidden;
    box-shadow: 0 14px 30px rgba(0,0,0,0.45);
  }

  /* ---------- shared wordmark ---------- */
  .brand {
    display: flex; align-items: center; justify-content: center; gap: 12px;
    font-weight: 600; letter-spacing: 0.3px; white-space: nowrap;
  }
  .brand__dot { border-radius: 50%; flex: none; }

  /* ---------- back of card ---------- */
  .card--back { top: 40px; background: var(--navy); }
  .back-identity {
    position: absolute; left: 0; right: 0; top: 140px; text-align: center;
  }
  .card--back .brand { color: var(--white); font-size: 44px; }
  .card--back .brand__dot { width: 30px; height: 30px; background: var(--white); }
  .slogan {
    margin-top: 8px; color: var(--ink-soft);
    font-size: 15px; letter-spacing: 2px; text-transform: uppercase;
  }
  .back-rule {
    position: absolute; left: 0; right: 0; bottom: 52px;
    border-top: 1.5px dashed rgba(255,255,255,0.75);
  }
  .back-web {
    position: absolute; right: 44px; bottom: 62px;
    color: var(--white); font-size: 17px; letter-spacing: 0.5px;
  }

  /* ---------- front of card ---------- */
  .card--front { top: 480px; background: var(--paper); }
  .front-shapes { position: absolute; inset: 0; }
  .name-tab {
    position: absolute; left: 0; top: 92px; width: 32px; height: 46px;
    background: var(--white);
  }
  .person { position: absolute; left: 58px; top: 78px; }
  .person__name {
    color: var(--orange); font-weight: 700; font-size: 38px; line-height: 1.05;
    letter-spacing: 0.5px;
  }
  .person__title { color: var(--white); font-size: 22px; margin-top: 2px; }
  .contacts {
    position: absolute; left: 62px; top: 206px; list-style: none;
    color: var(--white); font-size: 17px; letter-spacing: 0.3px;
  }
  .contacts li { display: flex; align-items: center; gap: 14px; height: 33px; }
  .contacts svg { width: 20px; height: 20px; flex: none; }

  .front-identity {
    position: absolute; left: 478px; top: 112px; width: 205px; text-align: center;
  }
  .card--front .brand { color: var(--navy); font-size: 22px; gap: 8px; }
  .card--front .brand__dot { width: 16px; height: 16px; background: var(--orange); }
  .social {
    position: absolute; left: 480px; top: 248px; width: 200px; text-align: center;
  }
  .social__label {
    color: var(--orange); font-size: 10px; font-weight: 600; letter-spacing: 0.4px;
    white-space: nowrap;
  }
  .social__icons { display: flex; justify-content: center; gap: 16px; margin-top: 12px; }
  .social__icon {
    width: 32px; height: 32px; border-radius: 50%;
    border: 2px solid var(--orange);
  }
</style>
</head>
<body>
<main class="sheet">

  <section class="card card--back" aria-label="Card back">
    <div class="back-identity">
      <div class="brand"><span class="brand__dot"></span>Vantrel Systems</div>
      <p class="slogan">Industrial Automation and Control</p>
    </div>
    <div class="back-rule"></div>
    <div class="back-web">www.vantrelsystems.example</div>
  </section>

  <section class="card card--front" aria-label="Card front">
    <svg class="front-shapes" viewBox="0 0 700 400" width="700" height="400" aria-hidden="true">
      <path d="M0 0 H320 C410 70 420 260 335 400 H0 Z" fill="var(--navy)"/>
      <path d="M372 0 H400 C475 80 485 280 358 400 H345 C455 270 445 80 372 0 Z" fill="var(--orange)"/>
    </svg>

    <div class="name-tab"></div>
    <div class="person">
      <h1 class="person__name">Declan Hart</h1>
      <p class="person__title">Founder &amp; CEO</p>
    </div>

    <ul class="contacts">
      <li>
        <svg viewBox="0 0 24 24"><path fill="#fff" d="M6.6 10.8a15 15 0 0 0 6.6 6.6l2.2-2.2c.3-.3.7-.4 1-.2 1.1.4 2.3.6 3.6.6.6 0 1 .4 1 1V20c0 .6-.4 1-1 1A17 17 0 0 1 3 4c0-.6.4-1 1-1h3.5c.6 0 1 .4 1 1 0 1.3.2 2.5.6 3.6.1.3 0 .7-.2 1z"/></svg>
        +44 555 010 2290
      </li>
      <li>
        <svg viewBox="0 0 24 24"><path fill="#fff" d="M2 11 22 2l-9 20-2.5-8.5z"/></svg>
        info@vantrelsystems.example
      </li>
      <li>
        <svg viewBox="0 0 24 24" fill="none" stroke="#fff" stroke-width="1.8"><circle cx="12" cy="12" r="9"/><path d="M3 12h18M12 3c3 3 3 15 0 18M12 3c-3 3-3 15 0 18"/></svg>
        www.vantrelsystems.example
      </li>
      <li>
        <svg viewBox="0 0 24 24"><path fill="#fff" d="M12 2a7 7 0 0 0-7 7c0 5 7 13 7 13s7-8 7-13a7 7 0 0 0-7-7zm0 9.5A2.5 2.5 0 1 1 12 6.5a2.5 2.5 0 0 1 0 5z"/></svg>
        Street, Address, Country
      </li>
    </ul>

    <div class="front-identity">
      <div class="brand"><span class="brand__dot"></span>Vantrel Systems</div>
    </div>

    <div class="social">
      <p class="social__label">FIND US ON SOCIAL MEDIA</p>
      <div class="social__icons">
        <span class="social__icon"></span>
        <span class="social__icon"></span>
        <span class="social__icon"></span>
      </div>
    </div>
  </section>

</main>
</body>
</html>
```